Real Estate - Large Sign Design

I am looking for a fresh new look for our leasing signs that will be showcase in front of commercial buildings available for lease. The sign dimension can be either 8'x4' or 4'x8'. They must exemplify our brand (see attachments) and be very visible by people driving by at high speeds.
They must include the following:
- Our logo (vector attached)
- Office Space Available
- 555-018-3274
- Nell Ruby
- Carl Ivey
- www.vantorile.com
Please let me know if you have any questions.
Target Market(s)
Drivers in high traffic areas, walking crowds
Industry/Entity Type
Real Estate
Requirements
Must have
- They must include the following:
- - Our logo (vector attached)
- - Office Space Available
- - 555-018-3274
- - Nell Ruby
- - Carl Ivey
- - www.vantorile.com
Should not have
- Should not be busy or hard to read.

```html
<!DOCTYPE html>
<html lang="en">
<head>
<meta charset="utf-8">
<title>Office Space Available – Leasing Sign</title>
<link rel="stylesheet" href="https://fonts.googleapis.com/css2?family=Abril+Fatface&family=Anton&family=Archivo+Black&family=Archivo:wght@500&display=swap">
<style>
  :root {
    --green-bright: #5cff0a;
    --green-edge: #3fee00;
    --green-glow: #8dff2a;
    --tower-dark: #4fc92a;
    --tower-light: #c8ff3a;
    --ink: #000000;
    --paper: #ffffff;
    --signal-yellow: #ffff00;
  }
  * { margin: 0; padding: 0; box-sizing: border-box; }
  html, body { width: 1200px; height: 601px; overflow: hidden; }
  body { background: var(--green-bright); }
  .sign {
    position: relative;
    width: 1200px;
    height: 601px;
    overflow: hidden;
    background: radial-gradient(ellipse at 45% 40%, var(--green-glow) 0%, var(--green-bright) 45%, var(--green-edge) 100%);
  }
  .skyline-art {
    position: absolute;
    left: 40px;
    top: 110px;
    width: 380px;
    height: 491px;
    background: linear-gradient(90deg, var(--tower-dark) 0%, #6fe040 40%, var(--tower-light) 60%, #a8f23a 100%);
    opacity: 0.85;
  }
  .brand-panel {
    position: absolute;
    left: 246px;
    top: 0;
    width: 346px;
    height: 202px;
    background: var(--ink);
    display: flex;
    flex-direction: column;
    justify-content: center;
    align-items: center;
    color: var(--paper);
    font-family: "Abril Fatface", serif;
    font-size: 42px;
    line-height: 1.05;
    text-align: center;
  }
  .copy { position: absolute; inset: 0; }
  .agents { font-family: "Abril Fatface", serif; font-size: 48px; fill: var(--ink); }
  .phone { font-family: "Archivo Black", sans-serif; font-size: 49px; fill: var(--signal-yellow); }
  .headline-top { font-family: "Anton", sans-serif; font-size: 92px; fill: var(--paper); }
  .headline-main { font-family: "Archivo Black", sans-serif; font-size: 118px; fill: var(--signal-yellow); }
  .web { font-family: "Archivo", sans-serif; font-weight: 500; font-size: 42px; fill: var(--ink); }
</style>
</head>
<body>
  <main class="sign">
    <div class="skyline-art" role="img" aria-label="Illustration of green office towers"></div>

    <div class="brand-panel">
      <span>Halvern</span>
      <span>Realty Group</span>
    </div>

    <svg class="copy" width="1200" height="601" viewBox="0 0 1200 601">
      <text class="agents" x="1172" y="64" text-anchor="end">Nell Ruby &amp;</text>
      <text class="agents" x="1172" y="113" text-anchor="end">Carl Ivey</text>
      <text class="phone" x="1182" y="175" text-anchor="end" textLength="346" lengthAdjust="spacingAndGlyphs">555-018-3274</text>
      <text class="headline-top" x="588" y="344" textLength="588" lengthAdjust="spacingAndGlyphs">OFFICE SPACE</text>
      <text class="headline-main" x="462" y="472" textLength="714" lengthAdjust="spacingAndGlyphs">AVAILABLE</text>
      <text class="web" x="584" y="554" textLength="592" lengthAdjust="spacing">www.vantorile.com</text>
    </svg>
  </main>
</body>
</html>
```